Ravelor Global Kft. is an online recruitment marketplace connecting the employers and recruiters together. We provide an e-bussiness solution for companies and give busines opportunity for recruiters.
We have a logo design already, which should be used on the business card.
Our colours are grey and magenta, which can be seen in the logo. Black is also welcome.
The style should be dynamic, young but professional. It should be clear, visible, elegant, not too crowded, simple but exciting.
We need the following data on the BC: name, title, address, phone,fax and mobile number, email address, website.
Target Market(s)
Our target market are companies, as this is a B2B business. We also target recruiters, recruitment professionals, headhunters.We would like to be impressive and different.
Industry/Entity Type
Business
Requirements
Must have
- We would like to promote our website, www.ravelorglb.hu.
- Please, put this on the back with a quite visible letter size.The style should be dynamic, young but professional. It should be clear, visible, elegant, not too crowded, simple but exciting.
Should not have
- We do not want to see people figures.

```html
<!DOCTYPE html>
<html lang="en">
<head>
<meta charset="utf-8">
<title>Ravelor Global Kft. – Business Card</title>
<link rel="stylesheet" href="https://fonts.googleapis.com/css2?family=Arimo:wght@400;700&family=Roboto+Condensed:wght@400&display=swap">
<style>
  :root {
    --page-bg: #ecebe8;
    --card-white: #ffffff;
    --magenta: #b51a6f;
    --magenta-dark: #9c1560;
    --magenta-light: #c52483;
    --grey-logo: #7d6f7c;
    --silver-light: #e4e4e4;
    --silver-mid: #b9b9b9;
    --silver-dark: #8c8c8c;
    --ink: #2b2b2b;
    --text-on-magenta: #ffffff;
  }
  * { margin: 0; padding: 0; box-sizing: border-box; }
  html, body {
    width: 1200px; height: 900px; overflow: hidden;
    background: var(--page-bg);
  }
  .card {
    position: absolute; left: 132px; top: 180px;
    width: 940px; height: 540px;
    background: var(--card-white);
    box-shadow: 0 6px 18px rgba(0,0,0,0.18);
    overflow: hidden;
    font-family: "Arimo", Arial, sans-serif;
  }
  .card__decor {
    position: absolute; left: 600px; top: 0;
    width: 340px; height: 230px;
    background: radial-gradient(ellipse at 60% 50%, #e6e6e6 0%, #f3f3f3 45%, rgba(255,255,255,0) 80%);
  }
  .brand {
    position: absolute; left: 194px; top: 250px;
    display: flex; align-items: center; gap: 22px;
  }
  .brand { left: 62px; top: 70px; }
  .brand__mark {
    width: 86px; height: 86px; background: var(--magenta);
  }
  .brand__name {
    font-family: "Arimo", Arial, sans-serif;
    font-weight: 700; font-size: 58px; letter-spacing: 1px;
    color: var(--magenta);
  }
  .name-band {
    position: absolute; left: 0; top: 230px;
    width: 940px; height: 50px;
    background: linear-gradient(90deg, var(--silver-mid) 0%, var(--silver-light) 30%, #fafafa 45%, var(--silver-mid) 62%, var(--silver-dark) 100%);
  }
  .name-band__title {
    position: absolute; left: 554px; top: 10px;
    font-family: "Roboto Condensed", "Arial Narrow", sans-serif;
    font-size: 27px; color: var(--ink); letter-spacing: 0.3px;
  }
  .contact-panel {
    position: absolute; left: 0; top: 280px;
    width: 940px; height: 260px;
    background: linear-gradient(90deg, var(--magenta-dark) 0%, var(--magenta) 40%, var(--magenta-light) 100%);
    color: var(--text-on-magenta);
  }
  .contact-panel__website {
    position: absolute; left: 48px; top: 176px;
    font-size: 24px; letter-spacing: 0.5px;
  }
  .contact-panel__details {
    position: absolute; left: 628px; top: 24px;
    font-size: 19px; line-height: 32px;
  }
  .contact-panel__details .gap { height: 12px; }
</style>
</head>
<body>
  <div class="card">
    <div class="card__decor" role="img" aria-label="Faint grey brand decoration"></div>
    <div class="brand">
      <div class="brand__mark"></div>
      <div class="brand__name">RAVELOR</div>
    </div>
    <div class="name-band">
      <div class="name-band__title">DANIEL. MARSH / OWNER</div>
    </div>
    <div class="contact-panel">
      <div class="contact-panel__details">
        <div>1820 Holloway Lane</div>
        <div>Bramford, TM 041270</div>
        <div class="gap"></div>
        <div>Phone : 1-834-555-0148</div>
        <div>Fax : 1-834-555-0149</div>
        <div>info@ravelorglb.com</div>
      </div>
      <div class="contact-panel__website">www.ravelorglb.hu</div>
    </div>
  </div>
</body>
</html>
```